Trailbend Gear Depot

Design a new website design for www.trailbendgeardepot.com,

Target Market(s)

Men & Ladies

Industry/Entity Type

Side X side, ATV Offroad

Coding

Coded - Design and coding required

Number of Pages Required

1 page

```html
<!DOCTYPE html>
<html lang="en">
<head>
<meta charset="utf-8">
<title>Trailbend Gear Depot</title>
<link href="https://fonts.googleapis.com/css2?family=Poppins:wght@300;400;500;600;700&family=Archivo+Black&display=swap" rel="stylesheet">
<style>
:root{
  --ink:#111;
  --black:#000;
  --coral:#f4604a;
  --grey:#8a8a8a;
  --light:#f4f4f4;
  --white:#fff;
}
*{box-sizing:border-box;margin:0;padding:0}
html,body{width:1200px;height:4411px;overflow:hidden}
body{position:relative;font-family:'Poppins',sans-serif;color:var(--ink);background:var(--white)}
.abs{position:absolute}
.brandmark{font-weight:700;color:var(--ink);line-height:1.05;font-size:26px}
.search{left:271px;top:38px;width:641px;height:58px;border:2px solid #ddd;display:flex}
.search span{flex:1;font-size:13px;color:#999;padding:19px 32px}
.search .btn{width:100px;background:var(--black);display:flex;align-items:center;justify-content:center}
.sidebar{left:0;top:123px;width:314px;height:640px;background:var(--black);padding:110px 0 0 40px}
.sidebar p{color:var(--white);font-weight:700;font-size:28px;margin-bottom:34px;letter-spacing:.5px}
.hero-photo{left:317px;top:123px;width:883px;height:640px;background:linear-gradient(90deg,#f1f1f1 0%,#d9d9d9 45%,#6b6b66 75%,#3c3c38 100%)}
.hero-title{left:362px;top:245px;font-family:'Archivo Black',sans-serif;font-size:53px;line-height:70px;color:var(--black);white-space:nowrap}
.hero-text{left:362px;top:395px;width:370px;font-size:12.5px;line-height:1.3;color:#222}
.btn-coral{background:var(--coral);color:var(--white);font-weight:500;display:flex;align-items:center;justify-content:center}
.promo-img{background:linear-gradient(120deg,#2a2a2a,#5a4a3d 55%,#2c2b2a)}
.promo-text{text-align:right;color:var(--white)}
.promo-text h3{font-weight:600;line-height:1.1}
.promo-text p{font-size:13px;margin-top:10px;white-space:nowrap}
.promo-text .btn-coral{display:inline-flex;margin-top:18px}
.label{width:1200px;text-align:center;color:var(--coral);font-size:12px;font-weight:600;letter-spacing:2px}
.title{width:1200px;text-align:center;font-size:35px;font-weight:500;color:var(--ink)}
.card{background:var(--white);box-shadow:0 2px 14px rgba(0,0,0,.1);text-align:center}
.card .ph{margin:18px auto 0;height:210px;width:84%;border-radius:6px;background:linear-gradient(150deg,#f2eeea 0%,#ddd3ca 50%,#c9bdb2 100%)}
.card h4{font-size:13px;font-weight:600;line-height:1.35;padding:0 10px;margin-top:20px}
.price{font-size:12px;margin-top:6px;color:var(--coral)}
.price s{color:#e8a69b;margin-right:4px}
.price b{font-weight:600;text-decoration:underline}
.cart{display:inline-block;background:var(--black);color:var(--white);font-size:13px;font-weight:600;padding:8px 20px;margin-top:14px}
.sale{position:absolute;right:6px;top:-4px;width:38px;height:38px;border-radius:50%;background:var(--coral);color:var(--white);font-size:11px;font-weight:600;display:flex;align-items:center;justify-content:center}
.flash-bg{left:0;top:1748px;width:1200px;height:566px;background:linear-gradient(180deg,#3c3f3d,#2b2e2b 60%,#373a36)}
.count{text-align:center;color:var(--coral)}
.count b{display:block;font-size:44px;font-weight:500;line-height:1}
.count span{font-size:13px}
.testi-bg{left:0;top:2991px;width:1200px;height:415px;background:linear-gradient(90deg,#2e2f31 0%,#6b6b6a 50%,#bdbcb9 100%)}
.tcard{background:var(--white);padding:28px 26px}
.stars{color:var(--coral);font-size:17px;letter-spacing:6px}
.tcard p{font-size:13px;color:#aaa;line-height:1.6;margin-top:18px}
.avatar{width:56px;height:56px;border-radius:50%;background:linear-gradient(#7d8894,#4a5561)}
.partner{width:163px;height:163px;border-radius:50%;background:#231f20;color:var(--white);display:flex;align-items:center;justify-content:center;font-weight:700;font-size:22px}
.footer{left:0;top:4076px;width:1200px;height:335px;background:var(--black);color:var(--white)}
.flabel{color:var(--coral);font-size:11px;font-weight:600;letter-spacing:1.5px}
.pay{width:24px;height:15px;border-radius:2px;display:inline-block;margin-left:4px}
</style>
</head>
<body>

<header>
  <div class="abs brandmark" style="left:37px;top:16px">TRAILBEND<br>GEAR<br>DEPOT</div>
  <div class="abs search"><span>What are you looking for.....</span>
    <div class="btn"><svg width="30" height="30" viewBox="0 0 30 30"><circle cx="13" cy="13" r="9" fill="none" stroke="#f4604a" stroke-width="2.5"/><line x1="20" y1="20" x2="27" y2="27" stroke="#f4604a" stroke-width="2.5"/></svg></div>
  </div>
  <svg class="abs" style="left:996px;top:42px" width="44" height="44" viewBox="0 0 44 44"><path d="M6 16h26l-2 24H8z" fill="none" stroke="#f4604a" stroke-width="2.5"/><path d="M13 16v-4a6 6 0 0 1 12 0v4" fill="none" stroke="#f4604a" stroke-width="2.5"/><circle cx="34" cy="12" r="10" fill="#000"/><text x="34" y="16" font-size="11" fill="#fff" text-anchor="middle" font-family="Poppins,sans-serif">0</text></svg>
  <svg class="abs" style="left:1066px;top:47px" width="36" height="36" viewBox="0 0 36 36"><circle cx="18" cy="18" r="16" fill="none" stroke="#f4604a" stroke-width="2.2"/><circle cx="18" cy="14" r="5" fill="none" stroke="#f4604a" stroke-width="2.2"/><path d="M8 29c3-6 17-6 20 0" fill="none" stroke="#f4604a" stroke-width="2.2"/></svg>
  <div class="abs" style="left:1110px;top:54px;font-size:15px;font-weight:500">Login</div>
</header>

<section>
  <nav class="abs sidebar">
    <p>RIDGEWAY</p><p>KESTREL</p><p>SORANO</p><p>YARROW</p><p>PINECREST</p><p>CANTOR</p>
  </nav>
  <div class="abs hero-photo" role="img" aria-label="Muddy side-by-side ATV parked on a dirt track among bare trees"></div>
  <h1 class="abs hero-title">HIGH QUALITY<br>ATV PRODUCTS</h1>
  <p class="abs hero-text">Lorem ipsum dolor sit amet, consectetur adipiscing elit. Ut elit tellus, luctus nec ullamcorper mattis, pulvinar dapibus leo.</p>
  <div class="abs btn-coral" style="left:363px;top:477px;width:225px;height:51px;font-size:24px">SHOP NOW</div>
</section>

<section>
  <div class="abs promo-img" style="left:36px;top:826px;width:622px;height:285px" role="img" aria-label="Side-by-side UTV jumping over dunes at dusk"></div>
  <div class="abs promo-text" style="left:300px;top:888px;width:308px">
    <h3 style="font-size:44px">New Arrivals</h3>
    <p>Discount up to 20% for Latest Parts</p>
    <div class="btn-coral" style="width:164px;height:36px;font-size:18px">SHOP NOW</div>
  </div>

  <div class="abs promo-img" style="left:696px;top:826px;width:432px;height:285px" role="img" aria-label="Green sport side-by-side on a dirt field"></div>
  <div class="abs promo-text" style="left:820px;top:878px;width:280px">
    <h3 style="font-size:40px">ON SALE</h3>
    <p>Discount up to 20% for Latest Parts</p>
    <div class="btn-coral" style="width:165px;height:38px;font-size:18px">SHOP NOW</div>
  </div>
</section>

<section>
  <div class="abs label" style="left:-6px;top:1187px">LATEST PRODUCT</div>
  <h2 class="abs title" style="left:-6px;top:1212px">New Arrival Product</h2>

  <div class="abs card" style="left:86px;top:1272px;width:240px;height:408px"><span class="sale">Sale!</span>
    <div class="ph" role="img" aria-label="Transmission gear and splined shaft"></div>
    <h4>Ridgeback, Turbo, Rover, Scout, or Apex 19% Gear Reduction</h4>
    <div class="price"><s>$700.00</s><b>$649.99</b></div><span class="cart">Add to cart</span></div>
  <div class="abs card" style="left:345px;top:1272px;width:240px;height:408px"><span class="sale">Sale!</span>
    <div class="ph" role="img" aria-label="Helical gear with two bearings"></div>
    <h4>Pinecrest Turf Mode Delete / Ridgeback 900, 1000 / Rover 900, 1000 / Scout</h4>
    <div class="price"><s>$320.00</s><b>$299.99</b></div><span class="cart">Add to cart</span></div>
  <div class="abs card" style="left:603px;top:1272px;width:240px;height:408px">
    <div class="ph" role="img" aria-label="Primary clutch gear set with springs"></div>
    <h4>Reduction 420/500/520 Primary 60% Rambler Pilgrim Ridgeline Foreland</h4>
    <div class="price" style="color:#e8a69b">$699.99</div><span class="cart">Add to cart</span></div>
  <div class="abs card" style="left:860px;top:1272px;width:242px;height:408px">
    <div class="ph" role="img" aria-label="Pair of meshed gears"></div>
    <h4>Rambler Pilgrim Ridgeline Foreland</h4>
    <div class="price" style="color:#e8a69b">$399.99</div><span class="cart">Add to cart</span></div>
</section>

<section>
  <div class="abs flash-bg" role="img" aria-label="Dark field with off-road vehicles in the background"></div>
  <div class="abs" style="left:75px;top:1822px;width:396px;height:444px;background:#fff"></div>
  <svg class="abs" style="left:110px;top:1908px" width="32" height="48" viewBox="0 0 32 48"><path d="M20 2L4 28h12L10 46l18-28H16z" fill="none" stroke="#f4604a" stroke-width="2"/></svg>
  <div class="abs" style="left:166px;top:1896px;font-size:37px;font-weight:500">Flash Deal</div>
  <p class="abs" style="left:166px;top:1956px;width:280px;font-size:14px;color:#999;line-height:1.55">Get Super Offer Only 2 Hours. Discount Up to 50% Just For You.</p>
  <div class="abs" style="left:176px;top:2028px;width:194px;height:42px;background:#000;color:#fff;font-size:14px;font-weight:600;display:flex;align-items:center;justify-content:center">More Info Flash Deal</div>
  <div class="abs count" style="left:110px;top:2108px;width:76px"><b>17</b><span>Hours</span></div>
  <div class="abs count" style="left:236px;top:2108px;width:76px"><b>24</b><span>Minutes</span></div>
  <div class="abs count" style="left:358px;top:2108px;width:76px"><b>51</b><span>Seconds</span></div>

  <div class="abs card" style="left:500px;top:1822px;width:295px;height:444px"><span class="sale">Sale!</span>
    <div class="ph" style="height:250px" role="img" aria-label="Transmission gear and splined shaft"></div>
    <h4>Ridgeback, Turbo, Rover, Scout, or Apex 19% Gear Reduction</h4>
    <div class="price"><s>$700.00</s><b>$649.99</b></div><span class="cart">Add to cart</span></div>
  <div class="abs card" style="left:816px;top:1822px;width:295px;height:444px"><span class="sale">Sale!</span>
    <div class="ph" style="height:250px" role="img" aria-label="Helical gear with two bearings"></div>
    <h4>Pinecrest Turf Mode Delete / Ridgeback 900, 1000 / Rover 900, 1000 / Scout</h4>
    <div class="price"><s>$320.00</s><b>$299.99</b></div><span class="cart">Add to cart</span></div>
</section>

<section>
  <div class="abs label" style="left:-17px;top:2385px">ON SALE PRODUCT</div>
  <h2 class="abs title" style="left:-17px;top:2412px">Best Seller Product</h2>

  <div class="abs card" style="left:57px;top:2473px;width:248px;height:424px"><span class="sale">Sale!</span>
    <div class="ph" role="img" aria-label="Transmission gear and splined shaft"></div>
    <h4>Ridgeback, Turbo, Rover, Scout, or Apex 19% Gear Reduction</h4>
    <div class="price"><s>$700.00</s><b>$649.99</b></div><span class="cart">Add to cart</span></div>
  <div class="abs card" style="left:324px;top:2473px;width:249px;height:424px"><span class="sale">Sale!</span>
    <div class="ph" role="img" aria-label="Helical gear with two bearings"></div>
    <h4>Pinecrest Turf Mode Delete / Ridgeback 900, 1000 / Rover 900, 1000 / Scout</h4>
    <div class="price"><s>$320.00</s><b>$299.99</b></div><span class="cart">Add to cart</span></div>
  <div class="abs card" style="left:593px;top:2473px;width:249px;height:424px">
    <div class="ph" role="img" aria-label="Primary clutch gear set with springs"></div>
    <h4>Reduction 420/500/520 Primary 60% Rambler Pilgrim Ridgeline Foreland</h4>
    <div class="price" style="color:#e8a69b">$699.99</div><span class="cart">Add to cart</span></div>
  <div class="abs card" style="left:860px;top:2473px;width:249px;height:424px">
    <div class="ph" role="img" aria-label="Pair of meshed gears"></div>
    <h4>Rambler Pilgrim Ridgeline Foreland</h4>
    <div class="price" style="color:#e8a69b">$399.99</div><span class="cart">Add to cart</span></div>
</section>

<section>
  <div class="abs testi-bg" role="img" aria-label="Off-road vehicles on a trail, faded"></div>
  <div class="abs" style="left:108px;top:3120px;color:#fff;font-size:11px;font-weight:600;letter-spacing:2px">TESTIMONIAL</div>
  <h2 class="abs" style="left:108px;top:3143px;color:#fff;font-size:34px;font-weight:600">What They Say</h2>
  <p class="abs" style="left:108px;top:3205px;width:270px;color:#f0c7bd;font-size:13.5px;line-height:1.5">Lorem ipsum dolor sit amet, consectetur adipiscing elit. Ut elit tellus, luctus nec ullamcorper mattis, pulvinar dapibus leo.</p>

  <div class="abs tcard" style="left:408px;top:3063px;width:329px;height:274px">
    <div class="stars">★★★★★</div>
    <p>Egestas sit eget platea justo sodales pulvinar tristique eleifend nam libero. Sagittis natoque sed suspendisse consequat semper rhoncus habitasse class.</p>
    <div class="avatar abs" style="left:26px;top:196px" role="img" aria-label="Customer portrait"></div>
    <div class="abs" style="left:104px;top:204px;font-size:14px;font-weight:500">John Doe<br><span style="font-size:11px;color:#aaa;font-weight:400">Biker</span></div>
    <div class="abs" style="right:26px;top:190px;font-size:64px;font-weight:700;color:#f4604a;line-height:1">”</div>
  </div>
  <div class="abs tcard" style="left:749px;top:3063px;width:326px;height:274px">
    <div class="stars">★★★★★</div>
    <p>Egestas sit eget platea justo sodales pulvinar tristique eleifend nam libero. Sagittis natoque sed suspendisse consequat semper rhoncus habitasse class.</p>
    <div class="avatar abs" style="left:26px;top:196px" role="img" aria-label="Customer portrait"></div>
    <div class="abs" style="left:104px;top:204px;font-size:14px;font-weight:500">John Doe<br><span style="font-size:11px;color:#aaa;font-weight:400">Biker</span></div>
    <div class="abs" style="right:26px;top:190px;font-size:64px;font-weight:700;color:#f4604a;line-height:1">”</div>
  </div>
</section>

<section>
  <div class="abs label" style="left:-38px;top:3464px;font-size:18px;letter-spacing:3px">PARTNER</div>
  <h2 class="abs title" style="left:-38px;top:3500px;font-size:52px">Awesome Partner</h2>
  <div class="abs partner" style="left:110px;top:3624px">RIDGEWAY</div>
  <div class="abs partner" style="left:366px;top:3624px">KESTREL</div>
  <div class="abs partner" style="left:621px;top:3624px">SORANO</div>
  <div class="abs partner" style="left:875px;top:3624px">YARROW</div>
  <div class="abs partner" style="left:110px;top:3817px">PINECREST</div>
  <div class="abs partner" style="left:366px;top:3817px">CANTOR</div>
  <div class="abs partner" style="left:621px;top:3817px">SORANO</div>
  <div class="abs partner" style="left:875px;top:3817px">YARROW</div>
</section>

<footer class="abs footer">
  <div class="abs" style="left:50px;top:120px;font-size:17px;font-weight:600;line-height:1.1">TRAILBEND<br>GEAR DEPOT</div>
  <div class="abs" style="left:50px;top:176px;width:62px;height:2px;background:var(--coral)"></div>
  <div class="abs" style="left:56px;top:200px;display:flex;gap:18px">
    <span style="width:13px;height:13px;border-radius:50%;background:#fff"></span>
    <span style="width:13px;height:13px;border-radius:50%;background:#fff"></span>
    <span style="width:13px;height:13px;border-radius:50%;background:#fff"></span>
  </div>
  <div class="abs flabel" style="left:302px;top:108px">PHONE</div>
  <div class="abs" style="left:302px;top:130px;font-size:11px">+(00)12-3456-7890</div>
  <div class="abs flabel" style="left:302px;top:159px">EMAIL US</div>
  <div class="abs" style="left:302px;top:181px;font-size:11px">support@trailbendgeardepot.com</div>
  <div class="abs" style="left:302px;top:211px;width:66px;height:2px;background:var(--coral)"></div>
  <ul class="abs" style="left:528px;top:110px;list-style:none;font-size:13px;line-height:1.6">
    <li><span style="color:var(--coral)">●</span> Privacy Policy</li>
    <li><span style="color:var(--coral)">●</span> Returns Policy</li>
    <li><span style="color:var(--coral)">●</span> Contact</li>
    <li><span style="color:var(--coral)">●</span> FAQS</li>
  </ul>
  <div class="abs" style="left:780px;top:45px;width:1px;height:215px;background:#444"></div>
  <div class="abs" style="left:808px;top:118px;width:248px;height:33px;background:#fff;color:#aaa;font-size:11px;padding:9px 14px">Name</div>
  <div class="abs btn-coral" style="left:808px;top:160px;width:248px;height:33px;font-size:12px">SIGNUP NOW</div>
  <div class="abs" style="left:122px;top:285px;font-size:11px;color:#ccc">© 2024 Trailbend Gear Depot. All Rights Reserved.</div>
  <div class="abs" style="left:854px;top:281px">
    <span class="pay" style="background:#2f6ebd"></span><span class="pay" style="background:#fff"></span><span class="pay" style="background:#fff"></span><span class="pay" style="background:#2c5aa0"></span><span class="pay" style="background:#1a3e8c"></span><span class="pay" style="background:#6a4fc4"></span><span class="pay" style="background:#e0a13a"></span>
  </div>
</footer>

</body>
</html>
```